Bref créative
Brightwater Realty and Acreage
12%-20% guaranteed returns by law
I need double sided standard sized Business Card [3.5" x 2"]
Open to different fonts
Professional
Marcus Holt
C.E.O
Lakemont, USA,
info@brightwaterrealtyandacreage.com
Color of card should be blue. Lettering orange. Please check our website. The website is still under construction but it will give you ideas and colors etc. The logo was designed by Vexly!
Incorporate logo. 12%- 20% guaranteed returns by law. Worldwide opportunity. Offices in Carrowfield, USA, Lakemont, USA, Ashbridge, England, Kestrel Bay, Australia

```html
<!DOCTYPE html>
<html lang="en">
<head>
<meta charset="utf-8">
<title>Brightwater Realty and Acreage – Stationery</title>
<link rel="stylesheet" href="https://fonts.googleapis.com/css2?family=Open+Sans:wght@400;700;800&display=swap">
<style>
  :root {
    --bg: #eceef2;
    --paper: #ffffff;
    --blue: #2f5fc7;
    --navy: #1d2f6e;
    --gold: #e0a93a;
    --mist: #d9e1f5;
    --ink: #444a58;
  }
  * { box-sizing: border-box; margin: 0; padding: 0; }
  html, body {
    width: 1200px; height: 773px; overflow: hidden;
    background: var(--bg);
    font-family: "Open Sans", Arial, sans-serif;
    color: var(--ink);
  }
  .canvas { position: relative; width: 1200px; height: 773px; }

  .sheet {
    position: absolute; background: var(--paper); overflow: hidden;
    box-shadow: 0 2px 10px rgba(0,0,0,0.14);
  }

  .brand { position: absolute; display: flex; align-items: center; gap: 6px; white-space: nowrap; }
  .brand-dot { border-radius: 50%; background: var(--gold); flex: none; }
  .brand-name { font-weight: 800; color: var(--navy); letter-spacing: 0.5px; line-height: 1; }

  .contact { position: absolute; font-size: 6.5px; line-height: 1.5; color: var(--ink); white-space: nowrap; }
  .contact.right { text-align: right; }

  .wash {
    position: absolute; left: 0; bottom: 0;
    background: linear-gradient(30deg, var(--mist) 0%, rgba(217,225,245,0.45) 40%, rgba(255,255,255,0) 70%);
  }

  /* business cards */
  .card { left: 29px; width: 297px; height: 172px; border-radius: 16px; }
  .card-front { top: 211px; }
  .card-back { top: 403px; }
  .card .wash { width: 100%; height: 100%; }
  .person { position: absolute; right: 26px; top: 62px; text-align: right; }
  .person-name { font-size: 11px; font-weight: 700; color: var(--navy); }
  .person-title { font-size: 7px; color: var(--ink); }
  .card-front .contact { right: 26px; top: 96px; }

  .promo { position: absolute; left: 22px; top: 58px; }
  .promo-rate { font-size: 15px; font-weight: 800; color: var(--blue); line-height: 1.1; }
  .promo-line { font-size: 9px; font-weight: 700; color: var(--blue); }
  .promo-world { font-size: 11px; font-weight: 800; color: var(--blue); margin-top: 10px; }
  .offices { position: absolute; left: 22px; bottom: 14px; font-size: 6.5px; line-height: 1.45; }

  /* letterhead */
  .letterhead { left: 360px; top: 36px; width: 403px; height: 703px; }
  .letterhead .wash { width: 100%; height: 100%; }
  .letterhead .contact { right: 26px; bottom: 22px; }

  /* envelopes */
  .envelope-back { left: 588px; top: 197px; width: 583px; height: 247px; }
  .envelope-front { left: 629px; top: 331px; width: 542px; height: 286px; }
  .flap { position: absolute; left: 0; top: 0; width: 100%; height: 100%; }
  .envelope-front .wash { width: 100%; height: 100%; }
  .envelope-front .contact { right: 22px; bottom: 22px; }
</style>
</head>
<body>
<main class="canvas">

  <!-- Envelope, back -->
  <section class="sheet envelope-back" aria-label="Envelope back">
    <svg class="flap" viewBox="0 0 583 247" preserveAspectRatio="none" aria-hidden="true">
      <polygon points="0,0 583,0 583,14 291.5,112 0,14" fill="var(--blue)"/>
    </svg>
    <div class="brand" style="left:50%; top:52px; transform:translateX(-50%);">
      <span class="brand-dot" style="width:16px;height:16px;"></span>
    </div>
  </section>

  <!-- Envelope, front -->
  <section class="sheet envelope-front" aria-label="Envelope front">
    <div class="wash"></div>
    <div class="brand" style="right:22px; top:24px;">
      <span class="brand-dot" style="width:14px;height:14px;"></span>
      <span class="brand-name" style="font-size:14px;">BRIGHTWATER</span>
    </div>
    <div class="contact right">
      <p>Lakemont, USA</p>
      <p>Toll Free: 1-800-555-0142</p>
      <p>Phone: 813-555-0187</p>
      <p>email: info@brightwaterrealtyandacreage.com</p>
    </div>
  </section>

  <!-- Letterhead -->
  <section class="sheet letterhead" aria-label="Letterhead">
    <div class="wash"></div>
    <div class="brand" style="right:26px; top:28px;">
      <span class="brand-dot" style="width:16px;height:16px;"></span>
      <span class="brand-name" style="font-size:15px;">BRIGHTWATER</span>
    </div>
    <div class="contact right">
      <p>Lakemont, USA</p>
      <p>Toll Free: 1-800-555-0142</p>
      <p>Phone: 813-555-0187</p>
      <p>email: info@brightwaterrealtyandacreage.com</p>
      <p>www.brightwaterrealtyandacreage.com</p>
    </div>
  </section>

  <!-- Business card, front -->
  <section class="sheet card card-front" aria-label="Business card front">
    <div class="wash"></div>
    <div class="brand" style="right:26px; top:20px;">
      <span class="brand-dot" style="width:12px;height:12px;"></span>
      <span class="brand-name" style="font-size:12px;">BRIGHTWATER</span>
    </div>
    <div class="person">
      <p class="person-name">Marcus Holt</p>
      <p class="person-title">C.E.O</p>
    </div>
    <div class="contact right">
      <p>Lakemont, USA</p>
      <p>Toll Free: 1-800-555-0142</p>
      <p>Phone: 813-555-0187</p>
      <p>email: info@brightwaterrealtyandacreage.com</p>
      <p>www.brightwaterrealtyandacreage.com</p>
    </div>
  </section>

  <!-- Business card, back -->
  <section class="sheet card card-back" aria-label="Business card back">
    <div class="wash"></div>
    <div class="brand" style="left:22px; top:20px;">
      <span class="brand-dot" style="width:12px;height:12px;"></span>
      <span class="brand-name" style="font-size:12px;">BRIGHTWATER</span>
    </div>
    <div class="promo">
      <p class="promo-rate">12%-20%</p>
      <p class="promo-line">guaranteed returns by law</p>
      <p class="promo-world">Worldwide opportunity</p>
    </div>
    <div class="offices">
      <p>Carrowfield, USA</p>
      <p>Lakemont, USA</p>
      <p>Ashbridge, England</p>
      <p>Kestrel Bay, Australia</p>
    </div>
  </section>

</main>
</body>
</html>
```